Website design

we need to build up a web site for our newly established personal business (selling ladies accessories customized specifically for each buyer)
Currently we are on Instagram only but it is becoming more and more important to have a website go to our account at instagram to know more about the business: velaroze17

Regarding number of pages, please find them below but they might be
extended as the site gets bigger

- Email account ( 2 pages )
- Whats up icon ( 1 page )
- search icon ( 1 page it will be the result )
- Customer feed back ( 1 page with pictures )
- shipping icon ( 1 page )
- bank account details ( 1 page )
- Links ( Home - Hand made accessories - Gold Plated - Silver - Gift )
- Hand made Accessories ( many pages * more than 200 pages )
- Gold plated ( the same idea of the handmade accessories )
- Silver ( ( the same idea of the handmade accessories )
- Git ( the same idea of the handmade accessories )
- Cart page ( 1 page )
- latest picture ( Flash picture )
- Today's deals ( 1 page )
- Live chat area ( chat )
- sign your email area ( 1 page )

Target Market(s)

1- Ladies
2- Teenager girls
3- Male welling to gift female

Requirements
Must have
• 1- It must have an easy way to add more pictures on new products with their model numbers
2- It must have a shopping process from viewing the products, selecting / deselecting multiple products till check out and payment methode (either by credit card or by directly depositing in out account)
3- showing the seperate and accumalating prices as customers buying more products
4- feedback on each product
5- Clear icons at the front page for new products (changed periodically)
6- Ability to search
7- Showing prodcuts categories (like tradix and marketo)
8- a process to design the accossory by the buyer (selection field, dropdown list in each stage) example: select your "wrist size" (followed by dropdown list showing size in cm) then select "beads color" (followed by dropdown list showing available colors) seclect number of beads followed by dropdown list showing numbers etc.
9- it must be simple to avoide complications while shopping
10- It must accept Arabic language as many customers are arabic speakers
Nice to have

• 1- Reflects the ladies/femenen taste
2- New products icons should be shown at the main page and gets in and out in a smoothy way (not fast and rapid)
3- Modern feeling
4- it is better to have images while customer going through customizing the products to their need (eg. showing a hand wrist surronded by a measure while asking the customer to give the hand wrist size, etc.)

```html
<!DOCTYPE html>
<html lang="en">
<head>
<meta charset="utf-8">
<title>Velaroze Accessories</title>
<link href="https://fonts.googleapis.com/css2?family=Signika:wght@300;400;600&family=Cinzel:wght@400&display=swap" rel="stylesheet">
<style>
:root{
  --bg:#efe3c3;
  --bg-light:#f6eed8;
  --panel:#fdfbf4;
  --gold:#c9a14e;
  --gold-text:#b8893f;
  --brown:#6b4a1c;
  --nav:#8d8675;
  --nav-dark:#6f6857;
  --grey-text:#7d7666;
  --dark-text:#4a4436;
  --red:#d9393b;
  --field:#efe6c9;
  --pill:#eee2c8;
}
*{margin:0;padding:0;box-sizing:border-box}
html,body{width:1200px;height:1011px;overflow:hidden}
body{
  position:relative;
  font-family:"Signika",sans-serif;
  background:radial-gradient(ellipse at 50% 20%,var(--bg-light) 0%,var(--bg) 70%);
  color:var(--grey-text);
}
.abs{position:absolute}
.top-rule{left:0;top:0;width:1200px;height:6px;background:linear-gradient(#d9ccae,#efe3c3)}
.top-links{left:464px;top:22px;display:flex;gap:22px;font-size:12.5px;font-weight:300}
.top-links a{color:var(--grey-text);text-decoration:none;padding:2px 5px}
.top-links a.current{background:#a79f8c;color:#fff;border-radius:2px}
.live-chat{left:850px;top:8px;width:83px;height:22px;background:var(--red);color:#fff;border-radius:0 0 5px 5px;font-size:12.5px;font-weight:600;display:flex;align-items:center;justify-content:center;gap:6px}
.brand{left:200px;top:48px;font-size:30px;color:var(--gold-text);font-weight:400;display:flex;align-items:center;gap:8px}
.brand-dot{width:12px;height:12px;border-radius:50%;background:var(--gold)}
.brand-sub{left:290px;top:82px;font-size:12px;color:var(--gold-text);font-weight:300}
.main-nav{left:373px;top:91px;width:618px;height:30px;background:linear-gradient(#a39c8a,var(--nav));display:flex;align-items:center;font-size:12px;color:#fff;font-weight:300}
.main-nav span{height:30px;display:flex;align-items:center;padding:0 18px;border-right:1px solid #a9a291}
.main-nav .active{background:linear-gradient(#7a561f,#5e3f12)}
.search{margin-left:8px;width:110px;height:17px;border-radius:9px;background:#c9c2b0;border:1px solid #ddd6c4;position:relative}
.search svg{position:absolute;right:6px;top:3px}
.hero{left:171px;top:121px;width:820px;height:249px;background:linear-gradient(100deg,#efe3c3 0%,#eadbb9 35%,#d9bd98 60%,#c79e75 80%,#e8d6b8 100%)}
.hero-title{left:190px;top:228px;font-family:"Cinzel",serif;color:#6e6a5e;line-height:.9}
.hero-title .l1{font-size:24px}
.hero-title .l2{font-size:34px}
.slider-bar{left:171px;top:370px;width:820px;height:46px;background:rgba(210,190,150,.55)}
.dots{left:217px;top:385px;display:flex;gap:10px}
.dots span{width:18px;height:18px;background:#c8bca2;color:#fff;font-size:12px;display:flex;align-items:center;justify-content:center;font-weight:300}
.dots .on{background:var(--gold);outline:1px solid #fff;outline-offset:-2px}
.hero-base{left:171px;top:416px;width:820px;height:15px;background:#8b8573}
.content{left:171px;top:431px;width:820px;height:534px;background:linear-gradient(var(--panel),#faf6ea)}
.login{left:199px;top:455px;width:192px;height:128px;border:1px solid #efe5cc;border-radius:5px;background:#f9f2e0;font-size:11px;color:var(--dark-text)}
.login label{position:absolute;left:19px}
.field{position:absolute;left:14px;width:164px;height:20px;border-radius:10px;background:var(--field);border:1px solid #f4edd9;font-size:10px;color:#fff;padding:3px 14px;font-weight:300}
.go{position:absolute;right:-1px;top:0;width:24px;height:20px;border-radius:0 10px 10px 0;background:var(--brown);color:#fff;font-size:10px;display:flex;align-items:center;justify-content:center}
.date{left:197px;top:614px;width:28px;height:33px;border:1px solid #e4ddcd;background:#fff;font-size:8px;text-align:center;color:#8a8475}
.date b{display:block;background:var(--red);color:#fff;font-size:9px;font-weight:600;margin:2px 3px}
.news-rule{left:234px;top:614px;width:1px;height:38px;background:#e6dfce}
.news-title{left:245px;top:613px;width:150px;font-size:11.5px;color:var(--dark-text);line-height:14px}
.news-body{left:245px;top:656px;width:150px;font-size:11.5px;color:var(--gold-text);line-height:13.7px;font-weight:300}
.chatline{left:246px;top:829px;width:82px;height:79px;border:1px solid #ece5d6;border-radius:4px;background:#fff;display:flex;flex-direction:column;align-items:center;justify-content:center;gap:6px;font-size:11px;color:var(--dark-text)}
.chatline i{width:36px;height:36px;border-radius:50%;background:#3fa848}
.promo{top:455px;width:254px;height:127px;background:linear-gradient(#efe6cf,#fbf7ec 14px)}
.promo-img{position:absolute;top:14px;height:113px}
.p1{left:428px}.p2{left:711px}
.p1 .promo-img{left:0;width:128px;background:linear-gradient(120deg,#6a5a3e,#9b8766 40%,#7dc6c4 70%,#e9e1cf)}
.p2 .promo-img{right:0;width:110px;background:linear-gradient(150deg,#f5efdf,#d9c28a 50%,#f2ead6)}
.p1-text{position:absolute;left:132px;top:27px;color:var(--gold-text);font-weight:300}
.p1-text .big{font-size:17px;line-height:18px}
.p1-text .small{font-size:10px;line-height:10px}
.p2-text{position:absolute;left:30px;top:36px;color:var(--gold-text);font-size:15.5px;line-height:22px}
.p2-text .strong{font-weight:600}
.promo-copy{top:595px;width:250px;font-size:10.5px;line-height:18.2px;color:var(--gold-text);font-weight:300}
.pill{background:var(--pill);color:#b7a98a;font-size:8.5px;border-radius:7px;padding:1px 5px;font-weight:300}
.dash{left:431px;top:698px;width:529px;border-top:1px dashed #e6d7a8}
.collection-title{left:430px;top:711px;font-size:13px;color:var(--gold-text);font-weight:300}
.arrow{top:768px}
.thumb{top:736px;height:71px;border:1px solid #ebe2cc;background:#f6eed8}
.t1{left:458px;width:107px;background:linear-gradient(135deg,#e9dcc0,#c9b089 60%,#9a9c9a)}
.t2{left:595px;width:99px;background:linear-gradient(135deg,#eef2ec,#c7d3c9 50%,#8c7660)}
.t3{left:721px;width:98px}
.t4{left:844px;width:95px}
.item{top:822px;width:112px;font-size:9.4px;line-height:12px;color:var(--gold-text);font-weight:300}
.price{top:883px;font-size:9px;color:#cbbfa6;font-weight:300}
.cart{top:880px}
.item-more{top:918px}
.footer-line{left:171px;top:964px;width:224px;height:3px;background:var(--gold)}
.copyright{left:178px;top:982px;font-size:6.5px;color:#9d9584}
.footer-nav{left:628px;top:984px;display:flex;gap:18px;font-size:8px;color:#8a8271;font-weight:300}
.footer-nav .here{color:var(--gold-text);font-weight:400}
.to-top{left:943px;top:957px;width:28px;height:28px;background:var(--gold);border-radius:3px;display:flex;align-items:center;justify-content:center}
</style>
</head>
<body>
<div class="abs top-rule"></div>

<nav class="abs top-links"><a class="current">About Us</a><a>Locations</a><a>Site Map</a><a>Contact Us</a></nav>
<div class="abs live-chat">Live Chat <svg width="7" height="8"><path d="M0 0L7 4L0 8Z" fill="#fff"/></svg></div>

<div class="abs brand"><span class="brand-dot"></span>Velaroze</div>
<div class="abs brand-sub">Accessories</div>

<nav class="abs main-nav">
  <span>Home</span><span class="active">Hand made accessories</span><span>Gold Plated</span><span>Silver Plated</span><span style="border:none">Gift</span>
  <div class="search"><svg width="10" height="10"><circle cx="4" cy="4" r="3" stroke="#fff" stroke-width="1.5" fill="none"/><path d="M6 6L9 9" stroke="#fff" stroke-width="1.6"/></svg></div>
</nav>

<div class="abs hero" role="img" aria-label="Photograph of a woman with short hair wearing a bracelet"></div>
<div class="abs hero-title"><div class="l1">100% HAND MADE</div><div class="l2">ACCESSORIES</div></div>
<div class="abs slider-bar"></div>
<div class="abs dots"><span>1</span><span>2</span><span class="on">3</span><span>4</span><span>5</span></div>
<div class="abs hero-base"></div>

<div class="abs content"></div>

<form class="abs login">
  <label style="top:17px">User Name</label>
  <div class="field" style="top:36px">user name here ...</div>
  <label style="top:66px">Password</label>
  <div class="field" style="top:86px">password here ..<span class="go">GO</span></div>
</form>

<div class="abs date"><b>05</b>JUN</div>
<div class="abs news-rule"></div>
<div class="abs news-title">Non duis sint cupidatat in ipsum occaecat aliquip sit.</div>
<p class="abs news-body">sed, ut exercitation ullamco qui quis occaecat id ullamco. Qui magna labore dolor nulla, lorem amet ex culpa sit consectetur dolor cupidatat ut quis sint tempor, id tempor. Non aute excepteur dolore enim dolore.</p>

<div class="abs chatline"><i></i>ChatLine</div>

<div class="abs promo p1">
  <div class="promo-img" role="img" aria-label="Photograph of a bowl with turquoise and pearl bead necklaces"></div>
  <div class="p1-text"><div class="big">New</div><div class="small">Best 2012 Collections<br>for your beauty !</div></div>
</div>
<div class="abs promo p2">
  <div class="promo-img" role="img" aria-label="Photograph of gold bangles"></div>
  <div class="p2-text"><div class="strong">Best 2013 Collections</div><div>for Our Brand !</div></div>
</div>
<p class="abs promo-copy" style="left:429px">Pariatur aute enim veniam. Ut quis est quis ullamco consequat in amet. In tempor mollit velit veniam nisi. Elit eiusmod elit incididunt elit laboris nulla irure sit occaecat do dolore.</p>
<p class="abs promo-copy" style="left:713px">Pariatur aute enim veniam. Ut quis est quis ullamco consequat in amet. In tempor mollit velit veniam nisi. Elit eiusmod elit incididunt elit laboris nulla irure sit occaecat do dolore.</p>
<span class="abs pill" style="left:628px;top:667px">read more</span>
<span class="abs pill" style="left:907px;top:667px">read more</span>

<div class="abs dash"></div>
<div class="abs collection-title">COLLECTION</div>
<svg class="abs arrow" style="left:432px" width="10" height="16"><path d="M8 1L2 8L8 15" stroke="#cfc5b0" stroke-width="2.5" fill="none"/></svg>
<svg class="abs arrow" style="left:953px" width="10" height="16"><path d="M2 1L8 8L2 15" stroke="#cfc5b0" stroke-width="2.5" fill="none"/></svg>

<div class="abs thumb t1" role="img" aria-label="Photograph of a pendant necklace worn at the neck"></div>
<div class="abs thumb t2" role="img" aria-label="Photograph of a smoky stone pendant on a gold chain"></div>
<div class="abs thumb t3" role="img" aria-label="Product photograph"></div>
<div class="abs thumb t4" role="img" aria-label="Product photograph"></div>

<p class="abs item" style="left:458px">Eiusmod aute ut aute magna dolor est, laboris voluptate culpa in quis qui consectetur est amet in?</p>
<p class="abs item" style="left:594px">Eiusmod aute ut aute magna dolor est, laboris voluptate culpa in quis qui consectetur est amet in?</p>
<p class="abs item" style="left:721px">Eiusmod aute ut aute magna dolor est, laboris voluptate culpa in quis qui consectetur est amet in?</p>
<p class="abs item" style="left:845px">Eiusmod aute ut aute magna dolor est, laboris voluptate culpa in quis qui consectetur est amet in?</p>

<span class="abs price" style="left:458px">Price: 48 JD</span>
<span class="abs price" style="left:594px">Price: 20 JD</span>
<span class="abs price" style="left:721px">Price: 20 JD</span>
<span class="abs price" style="left:845px">Price: 33 JD</span>

<svg class="abs cart" style="left:541px" width="15" height="13"><path d="M0 1H3L5 9H13L14 3H4" stroke="#8a8271" stroke-width="1.3" fill="none"/><circle cx="6" cy="11.5" r="1.2" fill="#8a8271"/><circle cx="12" cy="11.5" r="1.2" fill="#8a8271"/></svg>
<svg class="abs cart" style="left:672px" width="15" height="13"><path d="M0 1H3L5 9H13L14 3H4" stroke="#8a8271" stroke-width="1.3" fill="none"/><circle cx="6" cy="11.5" r="1.2" fill="#8a8271"/><circle cx="12" cy="11.5" r="1.2" fill="#8a8271"/></svg>
<svg class="abs cart" style="left:797px" width="15" height="13"><path d="M0 1H3L5 9H13L14 3H4" stroke="#8a8271" stroke-width="1.3" fill="none"/><circle cx="6" cy="11.5" r="1.2" fill="#8a8271"/><circle cx="12" cy="11.5" r="1.2" fill="#8a8271"/></svg>
<svg class="abs cart" style="left:930px" width="15" height="13"><path d="M0 1H3L5 9H13L14 3H4" stroke="#8a8271" stroke-width="1.3" fill="none"/><circle cx="6" cy="11.5" r="1.2" fill="#8a8271"/><circle cx="12" cy="11.5" r="1.2" fill="#8a8271"/></svg>

<span class="abs pill item-more" style="left:476px">read more</span>
<span class="abs pill item-more" style="left:618px">read more</span>
<span class="abs pill item-more" style="left:733px">read more</span>
<span class="abs pill item-more" style="left:866px">read more</span>

<div class="abs footer-line"></div>
<div class="abs copyright">© Copyright 2013 Velaroze.</div>
<nav class="abs footer-nav"><span class="here">Home</span><span>Privacy Policy</span><span>Terms &amp; Conditions</span><span>Contact Us</span></nav>
<div class="abs to-top"><svg width="14" height="18"><path d="M7 17V2M2 7L7 2L12 7" stroke="#fff" stroke-width="1.5" fill="none"/></svg></div>
</body>
</html>
```